Quimby's Yard & Garden Center Business Card Update

I need an updated Business card design for my Lawn and Garden Center. We do Landscaping installs, Lawn Mowing, Snow Removal and also have a Garden Center Retail Division. I uploaded a few of our previous business cards to give an idea of what we are starting with. The main goal of this update is to simplify and modernize the business card, not all of the services that are on the previous cards has to be on the new one but I would still like to highlight our main services. There is also a sample of our logo that Can be used in the design.

Industry/Entity Type

Landscaping

Contact Information for Business Card

Morris Quimby
Morris@Quimbysyardandgarden.example
Business (555) 201-7784
Cell (555) 318-6092

Colors

Designer to choose colors to be used in the design.

Requirements
Must have
• Services Provided :
• Landscaping
• Lawn Maintenance
• Snow Removal
• Garden Center

```html
<!DOCTYPE html>
<html lang="en">
<head>
<meta charset="utf-8">
<title>Quimby's Yard &amp; Garden Center — Business Card</title>
<link href="https://fonts.googleapis.com/css2?family=Lato:wght@400;700&display=swap" rel="stylesheet">
<style>
  :root {
    --backdrop: #3a322d;
    --card: #07090a;
    --card-edge: #2d5a27;
    --green: #2f6a2a;
    --green-bright: #3c7d34;
    --white: #ffffff;
    --muted: #e6e6e6;
  }
  * { box-sizing: border-box; margin: 0; padding: 0; }
  html, body {
    width: 1200px; height: 847px; overflow: hidden;
    background: var(--backdrop);
    font-family: 'Lato', sans-serif;
  }
  .canvas { position: relative; width: 1200px; height: 847px; }

  .card {
    position: absolute;
    width: 540px; height: 309px;
    background: var(--card);
    border-bottom: 2px solid var(--card-edge);
    box-shadow: 0 12px 30px rgba(0,0,0,.45);
    overflow: hidden;
  }
  .card--front { left: 60px; top: 80px; }
  .card--back  { left: 600px; top: 455px; }

  .wordmark {
    display: flex; align-items: center; gap: 14px;
    color: var(--white); font-weight: 700;
  }
  .wordmark__dot {
    border-radius: 50%; background: var(--green); flex: none;
  }
  .card--front .wordmark {
    position: absolute; left: 0; right: 0; top: 0; bottom: 0;
    justify-content: center; font-size: 68px;
  }
  .card--front .wordmark__dot { width: 54px; height: 54px; }

  .card--back .wordmark {
    position: absolute; left: 44px; top: 100px; font-size: 40px;
  }
  .card--back .wordmark__dot { width: 34px; height: 34px; }

  .divider {
    position: absolute; left: 290px; top: 58px;
    width: 2px; height: 150px; background: var(--green);
  }

  .contact { position: absolute; left: 310px; top: 62px; color: var(--muted); }
  .contact__name { color: var(--green-bright); font-weight: 700; font-size: 24px; line-height: 1.1; }
  .contact__title { font-size: 13px; margin: 2px 0 10px; }
  .contact__list { list-style: none; font-size: 11.5px; line-height: 1.75; }
  .contact__list li { display: flex; align-items: center; gap: 7px; white-space: nowrap; }
  .contact__list svg { width: 11px; height: 11px; flex: none; fill: var(--green-bright); }

  .services {
    position: absolute; left: 0; right: 0; bottom: 30px;
    display: flex; justify-content: center; gap: 10px;
    color: var(--white); font-size: 15px; list-style: none;
  }
  .services li + li::before {
    content: "|"; color: var(--green-bright); margin-right: 10px;
  }
</style>
</head>
<body>
<main class="canvas">

  <section class="card card--front" aria-label="Card front">
    <div class="wordmark">
      <span class="wordmark__dot"></span>
      <span>Quimby's</span>
    </div>
  </section>

  <section class="card card--back" aria-label="Card back">
    <div class="wordmark">
      <span class="wordmark__dot"></span>
      <span>Quimby's</span>
    </div>

    <div class="divider"></div>

    <div class="contact">
      <p class="contact__name">Morris Quimby</p>
      <p class="contact__title">Founder &amp; CEO</p>
      <ul class="contact__list">
        <li>
          <svg viewBox="0 0 24 24"><path d="M6.6 10.8a15 15 0 0 0 6.6 6.6l2.2-2.2c.3-.3.7-.4 1-.2 1.1.4 2.3.6 3.6.6.6 0 1 .4 1 1V20c0 .6-.4 1-1 1A17 17 0 0 1 3 4c0-.6.4-1 1-1h3.5c.6 0 1 .4 1 1 0 1.3.2 2.5.6 3.6.1.3 0 .7-.2 1z"/></svg>
          (555) 201-7784
        </li>
        <li>
          <svg viewBox="0 0 24 24"><path d="M7 1h10a2 2 0 0 1 2 2v18a2 2 0 0 1-2 2H7a2 2 0 0 1-2-2V3a2 2 0 0 1 2-2zm0 3v14h10V4zm5 15.5a1 1 0 1 0 0 2 1 1 0 0 0 0-2z"/></svg>
          (555) 318-6092
        </li>
        <li>
          <svg viewBox="0 0 24 24"><path d="M2 5h20v14H2zm2 2v.5l8 5 8-5V7zm0 2.8V17h16V9.8l-8 5z"/></svg>
          Morris@Quimbysyardandgarden.example
        </li>
        <li>
          <svg viewBox="0 0 24 24"><path d="M12 2a10 10 0 1 0 0 20 10 10 0 0 0 0-20zm0 2c.9 1.2 1.6 2.8 1.9 5h-3.8c.3-2.2 1-3.8 1.9-5zM4.3 11h3.8c0 .7 0 1.3.1 2H4.3a8 8 0 0 1 0-2zm5.8 2V11h3.8v2zm5.9 0c.1-.7.1-1.3.1-2h3.6a8 8 0 0 1 0 2zm-3.9 7c-.9-1.2-1.6-2.8-1.9-5h3.8c-.3 2.2-1 3.8-1.9 5z"/></svg>
          www.Quimbysyardandgarden.example
        </li>
      </ul>
    </div>

    <ul class="services">
      <li>Landscaping</li>
      <li>Lawn Maintenance</li>
      <li>Snow Removal</li>
      <li>Garden Center</li>
    </ul>
  </section>

</main>
</body>
</html>
```